New corporate stationery design for UK train leasing company

In advance of an office move later this year we are looking to redesign all our corporate stationery (business cards, letterhead, compliment slips, envelopes etc) as well as small branded items (such as mouse mats, drink mats, etc).

We wish to keep the same logo and corporate colours but are looking for a modern, fresh look that will tie in our stationery more with the look of our website and our PowerPoint template. We have a strapline, "Track Crews, True Knowhow" that we would like to incorporate into the stationery design and also need to include a "TEMLO" logo on the bottom of the letterhead/compliment slips. We have two offices so will need letterhead and compliment slips with both addresses.

The files attached include different versions of our logo (the main one is the black with green halo, file 1 or 3), our brand guidelines summary (including Pantone colours), the TEMLO logo and PowerPoint template.

More information about the business can be found at www.fernholtrail.co.uk.

If you have any questions please let me know.

I look forward to seeing the designs!
Regards
Moira

Target Market(s)

Main audience are train operators, rail industry suppliers, passenger transport groups, government and other political organisations, financiers/lenders.

Industry/Entity Type

Business

```html
<!DOCTYPE html>
<html lang="en">
<head>
<meta charset="utf-8">
<title>Fernholt Rail – Stationery</title>
<link rel="stylesheet" href="https://fonts.googleapis.com/css2?family=Open+Sans:wght@400;600;700&family=Mulish:wght@300;400&display=swap">
<style>
  :root {
    --bg: #e8e8e8;
    --paper: #f7f7f7;
    --ink: #2f2f2f;
    --ink-soft: #555;
    --teal: #14937e;
    --navy: #2b2a6c;
    --rule: #14937e;
  }
  * { box-sizing: border-box; margin: 0; padding: 0; }
  html, body { width: 1200px; height: 795px; overflow: hidden; background: var(--bg); }
  body { font-family: "Open Sans", sans-serif; color: var(--ink); position: relative; }

  .sheet { position: absolute; background: var(--paper); box-shadow: 0 6px 18px rgba(0,0,0,.12); overflow: hidden; }
  .sheet::after { content: ""; position: absolute; left: 0; right: 0; bottom: 0; height: 7px; background: var(--teal); }

  /* brand block */
  .brand { position: absolute; text-align: left; }
  .brand-name { font-family: "Mulish", sans-serif; font-weight: 300; color: var(--ink); letter-spacing: 1px; white-space: nowrap; display: flex; align-items: center; gap: 8px; }
  .brand-dot { width: 10px; height: 10px; border-radius: 50%; background: var(--teal); display: inline-block; }
  .strapline { font-weight: 700; color: var(--ink); line-height: 1.2; }
  .contact { color: var(--ink); line-height: 1.45; }
  .contact b { color: var(--teal); font-weight: 700; margin-right: 4px; }
  .contact .web { color: var(--teal); font-weight: 700; }

  /* letterhead */
  .letterhead { left: 60px; top: 30px; width: 520px; height: 735px; }
  .letterhead .brand { right: 42px; top: 44px; width: 190px; }
  .letterhead .brand-name { font-size: 30px; }
  .letterhead .strapline { font-size: 7.5px; margin-top: 6px; }
  .letterhead .contact { font-size: 7px; margin-top: 4px; }

  .letter { position: absolute; left: 44px; top: 150px; width: 400px; font-size: 8px; line-height: 1.5; color: var(--ink-soft); }
  .letter .salutation { font-weight: 700; color: var(--ink); margin-bottom: 10px; }
  .letter p { margin-bottom: 9px; }
  .signature { width: 110px; height: 30px; margin-top: 18px; background: linear-gradient(90deg, #e6e6e6, #efefef); border-radius: 3px; }
  .signer { font-weight: 700; color: var(--ink); font-size: 8px; margin-top: 4px; }

  .footer { position: absolute; left: 44px; right: 30px; bottom: 24px; display: flex; align-items: flex-end; font-size: 6.5px; line-height: 1.45; color: var(--ink); }
  .footer .office { width: 170px; }
  .footer .office strong { font-weight: 700; display: block; }
  .footer .divider { width: 1px; height: 26px; background: var(--rule); margin: 0 14px; }
  .footer .registration { flex: 1; }
  .partner { font-weight: 700; color: var(--navy); font-size: 16px; display: flex; align-items: center; gap: 5px; letter-spacing: .5px; }
  .partner .mark { width: 9px; height: 9px; background: var(--navy); display: inline-block; }

  /* compliment slip */
  .slip { left: 620px; top: 266px; width: 540px; height: 262px; }
  .slip .brand { right: 40px; top: 26px; width: 190px; }
  .slip .brand-name { font-size: 30px; }
  .slip .strapline { font-size: 7.5px; margin-top: 6px; }
  .slip .contact { font-size: 7px; margin-top: 4px; }
  .compliments { position: absolute; left: 30px; top: 140px; font-family: "Mulish", sans-serif; font-weight: 300; color: var(--teal); font-size: 22px; }
  .slip .footer { left: 30px; right: 28px; bottom: 22px; font-size: 7px; }
  .slip .footer .office { width: 120px; margin-left: 130px; }
  .slip .footer .divider { height: 40px; }
</style>
</head>
<body>

<section class="sheet letterhead" aria-label="Letterhead">
  <div class="brand">
    <div class="brand-name"><span class="brand-dot"></span>Fernholt Rail</div>
    <div class="strapline">Track Crews,<br>True Knowhow</div>
    <div class="contact">
      <div><b>T</b>+44 (0)20 7946 0321</div>
      <div><b>E</b>communications@fernholtrail.co.uk</div>
      <div class="web">www.fernholtrail.co.uk</div>
    </div>
  </div>

  <article class="letter">
    <div class="salutation">Lorem ipsum,</div>
    <p>Cras mattis consectetur purus sit amet fermentum. Etiam porta sem malesuada magna mollis euismod. Integer posuere erat a ante venenatis dapibus posuere velit aliquet. Cras justo odio, dapibus ac facilisis in, egestas eget quam. Aenean eu leo quam. Pellentesque ornare sem lacinia quam venenatis vestibulum.</p>
    <p>Vivamus sagittis lacus vel augue laoreet rutrum faucibus dolor auctor. Donec sed odio dui. Etiam porta sem malesuada magna mollis euismod. Morbi leo risus, porta ac consectetur ac, vestibulum at eros. Nullam id dolor id nibh ultricies vehicula ut id elit.</p>
    <p>Donec id elit non mi porta gravida at eget metus. Fusce dapibus, tellus ac cursus commodo, tortor mauris condimentum nibh, ut fermentum massa justo sit amet risus. Cras justo odio, dapibus ac facilisis in, egestas eget quam. Cum sociis natoque penatibus et magnis dis parturient montes, nascetur ridiculus mus.</p>
    <p>Cum sociis natoque penatibus et magnis dis parturient montes, nascetur ridiculus mus. Curabitur blandit tempus porttitor. Aenean lacinia bibendum nulla sed consectetur. Lorem ipsum dolor sit amet, consectetur adipiscing elit.</p>
    <p>Cras justo odio, dapibus ac facilisis in, egestas eget quam. Morbi leo risus, porta ac consectetur ac, vestibulum at eros. Duis mollis, est non commodo luctus, nisi erat porttitor ligula, eget lacinia odio sem nec elit. Integer posuere erat a ante venenatis dapibus posuere velit aliquet. Vivamus sagittis lacus vel augue laoreet rutrum faucibus dolor auctor.</p>
    <div class="signature" role="img" aria-label="Handwritten signature"></div>
    <div class="signer">Company Director</div>
  </article>

  <footer class="footer">
    <div class="office"><strong>Registered Office</strong>48 Harrow Lane, London, SE4 7QT</div>
    <div class="divider"></div>
    <div class="registration">Registered in England and Wales<br>Company Number 4820197 | VAT Registration Number 0481552713</div>
    <div class="partner"><span class="mark"></span>TEMLO</div>
  </footer>
</section>

<section class="sheet slip" aria-label="Compliment slip">
  <div class="brand">
    <div class="brand-name"><span class="brand-dot"></span>Fernholt Rail</div>
    <div class="strapline">Track Crews,<br>True Knowhow</div>
    <div class="contact">
      <div><b>T</b>+44 (0)20 7946 0321</div>
      <div><b>E</b>communications@fernholtrail.co.uk</div>
      <div class="web">www.fernholtrail.co.uk</div>
    </div>
  </div>

  <div class="compliments">With compliments</div>

  <footer class="footer">
    <div class="office"><strong>Registered Office</strong>48 Harrow Lane,<br>London, SE4 7QT</div>
    <div class="divider"></div>
    <div class="registration">Registered in England and Wales<br>Company Number 4820197<br>VAT Registration Number 0481552713</div>
    <div class="partner"><span class="mark"></span>TEMLO</div>
  </footer>
</section>

</body>
</html>
```